Ferncrest Dental, LLC business card project

Business card to be designed with current logo.
Dental office- please keep design of card that looks clean and professional.
Please include the following info:
Ferncrest Dental, LLC
Dr. Lorna Pettigrew
2871 Marlowe Street
Bethlehem, PA 18093
610-555-0193
ferncrestdental.office@examplemail.test
Hello everyone-
Reason: Just got back from overseas- will look at all designs and provide feedback. Thank you!
Reason: Polling my friends for the final selection-
thank you to all those that participated- so many talented designers!

```html
<!DOCTYPE html>
<html lang="en">
<head>
<meta charset="utf-8">
<title>Ferncrest Dental, LLC — Business Card</title>
<link rel="stylesheet" href="https://fonts.googleapis.com/css2?family=Questrial&family=Open+Sans:ital,wght@1,700&display=swap">
<style>
  :root {
    --backdrop: #d9d9d7;
    --card-white: #f7f7f5;
    --brand-green: #5a9e38;
    --leaf-green: #a6c83a;
    --leaf-light: #c3dc5a;
    --tooth-white: #f2f2f0;
    --text-white: #ffffff;
    --rule: rgba(255,255,255,0.55);
    --shadow: rgba(0,0,0,0.18);
  }
  * { box-sizing: border-box; margin: 0; padding: 0; }
  html, body {
    width: 1200px; height: 985px; overflow: hidden;
    background: var(--backdrop);
  }
  .canvas { position: relative; width: 1200px; height: 985px; }
  .card {
    position: absolute; left: 250px; width: 700px; height: 400px;
    box-shadow: 0 6px 18px var(--shadow);
  }
  .card--front { top: 70px; background: var(--card-white); }
  .card--back { top: 515px; background: var(--brand-green); overflow: hidden; }

  .wordmark {
    position: absolute; left: 120px; top: 165px;
    display: flex; align-items: center; gap: 16px;
  }
  .wordmark__dot {
    width: 30px; height: 30px; border-radius: 50%;
    background: var(--leaf-green);
  }
  .wordmark__name {
    font-family: "Questrial", sans-serif; font-size: 48px;
    color: var(--brand-green); letter-spacing: -0.5px; white-space: nowrap;
  }

  .edge-stripe { position: absolute; left: 0; top: 0; width: 14px; height: 400px; }

  .scene-art {
    position: absolute; left: 380px; top: 40px; width: 290px; height: 175px;
    border-radius: 100px 100px 0 0;
    background: linear-gradient(90deg, var(--leaf-green) 0%, var(--leaf-light) 40%, var(--tooth-white) 75%, #dcdcd8 100%);
    opacity: 0.85;
  }

  .doctor-name {
    position: absolute; left: 60px; top: 150px; white-space: nowrap;
    font-family: "Questrial", sans-serif; font-size: 24px; color: var(--text-white);
  }
  .doctor-name strong {
    font-family: "Open Sans", sans-serif; font-style: italic; font-weight: 700;
  }
  .rule { position: absolute; height: 1px; background: var(--rule); }
  .rule--top { top: 195px; left: 36px; width: 320px; }
  .rule--bottom { top: 322px; left: 60px; width: 600px; }

  .contact {
    position: absolute; left: 36px; top: 218px; list-style: none;
    font-family: "Questrial", sans-serif; font-size: 15px; color: var(--text-white);
  }
  .contact li { display: flex; align-items: center; gap: 10px; height: 24px; white-space: nowrap; }
  .contact svg { width: 13px; height: 13px; flex: none; }

  .address {
    position: absolute; right: 40px; top: 334px; text-align: right;
    font-family: "Questrial", sans-serif; font-size: 16px; line-height: 24px;
    color: var(--text-white); font-style: normal;
  }
</style>
</head>
<body>
<main class="canvas">
  <section class="card card--front" aria-label="Card front">
    <div class="wordmark">
      <span class="wordmark__dot"></span>
      <span class="wordmark__name">Ferncrest Dental, LLC</span>
    </div>
  </section>

  <section class="card card--back" aria-label="Card back">
    <svg class="edge-stripe" viewBox="0 0 14 400" aria-hidden="true">
      <rect x="0" y="0" width="8" height="400" fill="var(--leaf-green)"/>
      <polygon points="8,140 14,150 8,160" fill="var(--leaf-green)"/>
    </svg>

    <div class="scene-art" role="img" aria-label="Illustration of two green trees and a large white tooth on a green hill"></div>

    <p class="doctor-name">Dr. <strong>Lorna Pettigrew</strong></p>
    <div class="rule rule--top"></div>

    <ul class="contact">
      <li>
        <svg viewBox="0 0 16 16" aria-hidden="true"><path d="M3 1h3l1 4-2 1c1 2 3 4 5 5l1-2 4 1v3c0 1-1 2-2 2C7 15 1 9 1 3c0-1 1-2 2-2z" fill="var(--leaf-light)"/></svg>
        610-555-0193
      </li>
      <li>
        <svg viewBox="0 0 16 16" aria-hidden="true"><rect x="1" y="3" width="14" height="10" fill="var(--leaf-light)"/><path d="M1 3l7 6 7-6" fill="none" stroke="var(--brand-green)" stroke-width="1.2"/></svg>
        ferncrestdental.office@examplemail.test
      </li>
    </ul>

    <div class="rule rule--bottom"></div>
    <address class="address">2871 Marlowe Street<br>Bethlehem, PA 18093</address>
  </section>
</main>
</body>
</html>
```